Zielgruppe
Elektro und Automatisierungstechnik
Zielgruppe: Industriekunden
Aufgabenstellung
Zweiseitig farbig
Querformat 8,5*5,5cm
modernes, innovatives und zuverlässiges Unternehmen
Vorhandenes Logo muss integriert werden. Siehe Anhang

```html
<!DOCTYPE html>
<html lang="de">
<head>
<meta charset="utf-8">
<title>Kolsin Elektrotechnik – Visitenkarte</title>
<link rel="stylesheet" href="https://fonts.googleapis.com/css2?family=Montserrat:wght@400;500;700&display=swap">
<style>
  :root {
    --bg: #e2e2e2;
    --navy: #173656;
    --white: #ffffff;
    --ink: #1f2327;
  }
  * { margin: 0; padding: 0; box-sizing: border-box; }
  html, body {
    width: 1200px; height: 1200px; overflow: hidden;
    background: var(--bg);
    font-family: "Montserrat", Arial, sans-serif;
  }
  .card {
    position: absolute;
    left: 322px;
    width: 555px;
    height: 359px;
  }
  .card--front { top: 180px; background: var(--white); }
  .card--back  { top: 600px; background: var(--navy); color: var(--white); }

  .wordmark {
    position: absolute;
    display: flex;
    align-items: center;
    gap: 12px;
    font-weight: 700;
    line-height: 1;
  }
  .wordmark__square { flex: none; }
  .wordmark__text { display: flex; flex-direction: column; }
  .wordmark__name { letter-spacing: 0.04em; }
  .wordmark__sub  { letter-spacing: 0.06em; margin-top: 6px; }

  .card--front .wordmark {
    left: 50%; top: 50%;
    transform: translate(-50%, -56%);
    color: var(--navy);
  }
  .card--front .wordmark__square { width: 22px; height: 22px; background: var(--navy); }
  .card--front .wordmark__name { font-size: 52px; }
  .card--front .wordmark__sub  { font-size: 19.5px; }

  .card--back .wordmark { left: 303px; top: 46px; color: var(--white); gap: 9px; }
  .card--back .wordmark__square { width: 15px; height: 15px; background: var(--white); }
  .card--back .wordmark__name { font-size: 35px; }
  .card--back .wordmark__sub  { font-size: 13.2px; margin-top: 4px; }

  .person { position: absolute; left: 33px; top: 151px; }
  .person__name { font-size: 20px; font-weight: 700; letter-spacing: 0.01em; }
  .person__role { font-size: 14px; font-weight: 400; margin-top: 8px; }

  .contact {
    position: absolute; left: 303px; top: 193px;
    font-size: 13px; line-height: 18.2px; font-weight: 400;
    letter-spacing: 0.02em;
  }
  .contact__company { font-weight: 700; }
  .contact__gap { height: 18px; }
</style>
</head>
<body>
  <section class="card card--front" aria-label="Vorderseite">
    <div class="wordmark">
      <span class="wordmark__square"></span>
      <span class="wordmark__text">
        <span class="wordmark__name">KOLSIN</span>
        <span class="wordmark__sub">ELEKTROTECHNIK</span>
      </span>
    </div>
  </section>

  <section class="card card--back" aria-label="Rückseite">
    <div class="wordmark">
      <span class="wordmark__square"></span>
      <span class="wordmark__text">
        <span class="wordmark__name">KOLSIN</span>
        <span class="wordmark__sub">ELEKTROTECHNIK</span>
      </span>
    </div>

    <div class="person">
      <p class="person__name">Bernhard Josef Kolsin</p>
      <p class="person__role">Geschäftsführer</p>
    </div>

    <address class="contact" style="font-style: normal;">
      <p class="contact__company">Kolsin Elektrotechnik GmbH</p>
      <p>Lindenweg 7</p>
      <p>88161 Moosried</p>
      <div class="contact__gap"></div>
      <p>+49 98 765 43 21</p>
      <p>kontakt@kolsin-elektrotechnik.de</p>
      <p>www.kolsin-elektrotechnik.de</p>
    </address>
  </section>
</body>
</html>
```